Präsentationsvorlagen für die Cloud-Plattform LumaDesk
Zielgruppe
Ich bin ein unabhängiger Berater für die Cloud-Plattform LumaDesk. Zielgruppe sind Unternehmen jeglicher Größe. Das Design sollte schlicht und aufgeräumt sein.
Aufgabenstellung
Dunkler Hintergrund und die Farben aus dem Logo sollten enthalten sein.

```html
<!DOCTYPE html>
<html lang="en">
<head>
<meta charset="utf-8">
<title>deskrise – LumaDesk presentation templates</title>
<link href="https://fonts.googleapis.com/css2?family=Lato:wght@400;700;900&display=swap" rel="stylesheet">
<style>
:root{
  --bg:#ffffff;
  --slide:#000000;
  --orange:#f07f2a;
  --blue:#1f6fb5;
  --white:#ffffff;
  --grey:#d8d8d8;
  --box:#3a3a3a;
}
*{box-sizing:border-box;margin:0;padding:0}
html,body{width:1200px;height:2400px;overflow:hidden;background:var(--bg)}
body{position:relative;font-family:'Lato',Arial,sans-serif;color:var(--white)}
.slide{position:absolute;width:572px;height:322px;background:var(--slide);overflow:hidden}
.col-l{left:16px}.col-r{left:612px}
.r1{top:62px}.r2{top:387px}.r3{top:713px}.r4{top:1041px}.r5{top:1365px}.r6{top:1689px}.r7{top:2016px}

.brand{font-weight:900;color:var(--orange);letter-spacing:.5px;display:flex;align-items:center;gap:6px}
.brand .dot{width:.55em;height:.55em;border-radius:50%;background:var(--blue)}

.photo{position:absolute;top:0;right:0;height:100%;border-left:4px solid var(--orange)}
.photo-ai{width:212px;background:radial-gradient(circle at 55% 45%,#c04fd8 0%,#2b6fd6 22%,#10263f 50%,#05070c 80%)}
.photo-puzzle{width:212px;background:radial-gradient(circle at 50% 50%,#f6c777 0%,#e08a3d 30%,#7a3c1a 65%,#2a1208 100%)}
.photo-gears{width:212px;background:radial-gradient(circle at 50% 35%,#b8845a 0%,#5d4b44 35%,#9fb4c8 70%,#dfe8f0 100%)}
.photo-victory{width:212px;background:linear-gradient(180deg,#f7efe2 0%,#f0cc95 45%,#c98a4d 75%,#5a3a22 100%)}
.photo-hero{width:212px;background:linear-gradient(180deg,#7fa0b8 0%,#c9b9a0 35%,#f0a860 60%,#a84d22 85%,#3b1e12 100%)}
.photo .brand{position:absolute;left:0;right:0;justify-content:center;font-size:20px}

.title-block{position:absolute;left:29px}
.title-block h1{font-weight:900;font-size:41px;letter-spacing:1px;line-height:1}
.title-block p{font-weight:700;font-size:16px;letter-spacing:1.4px;line-height:1.25;margin-top:8px;text-transform:uppercase}
.title-block p.lower{text-transform:none;font-weight:400;letter-spacing:1.2px;margin-top:4px}
.url-tag{position:absolute;left:0;height:27px;width:150px;background:var(--orange);border-left:12px solid var(--blue);
  font-size:8px;font-weight:700;display:flex;align-items:center;padding-left:9px;letter-spacing:.2px}

.centered-title{position:absolute;left:0;right:0;text-align:center;font-weight:900;letter-spacing:.5px}

.bio-photo{position:absolute;left:210px;top:73px;width:154px;height:152px;background:var(--orange);
  clip-path:polygon(12% 0,88% 0,100% 14%,100% 88%,88% 100%,12% 100%,0 88%,0 12%)}
.bio-photo .inner{position:absolute;inset:4px;background:linear-gradient(180deg,#e4e4e4 0%,#b9b9bd 55%,#2c3f66 100%);
  clip-path:polygon(12% 0,88% 0,100% 14%,100% 88%,88% 100%,12% 100%,0 88%,0 12%)}
.bio-text{position:absolute;left:22px;right:22px;top:238px;font-size:6.6px;line-height:1.9;text-align:center;color:var(--grey)}

.timeline-line{position:absolute;left:282px;width:7px;background:var(--orange)}
.year{position:absolute;left:265px;width:41px;height:41px;border-radius:50%;background:var(--orange);
  font-weight:700;font-size:13px;display:flex;align-items:center;justify-content:center}
.tl-box{position:absolute;background:var(--box);border:2px solid var(--orange);font-size:6px;line-height:2.1;text-align:center;padding:4px 8px;color:var(--white)}
.tl-box::after{content:"";position:absolute;top:50%;transform:translateY(-50%);border:9px solid transparent}
.tl-box.right-arrow::after{right:-20px;border-left:11px solid var(--orange)}
.tl-box.left-arrow::after{left:-20px;border-right:11px solid var(--orange)}
.intro{position:absolute;left:90px;right:90px;top:53px;font-size:6px;line-height:1.3;text-align:center;color:var(--grey)}

.cert-col{position:absolute;top:94px}
.cert-col h3{font-size:11px;letter-spacing:2.4px;font-weight:700;margin-bottom:10px}
.cert-col li{list-style:none;font-size:7.2px;line-height:20px;padding-left:11px;position:relative;color:var(--grey)}
.cert-col li::before{content:"\2713";position:absolute;left:0;color:var(--orange);font-size:7px}
.cert-badge{position:absolute;left:419px;top:88px}

.portfolio-title{position:absolute;left:0;right:0;top:20px;text-align:center;font-weight:900;font-size:29px}
.portfolio-brand{position:absolute;right:28px;top:40px;font-size:16px}
.service{position:absolute;top:96px;width:236px}
.service .label{height:60px;background:var(--orange);border-radius:3px;display:flex;align-items:center;gap:14px;padding:0 12px;
  box-shadow:0 0 10px rgba(240,127,42,.35)}
.service .label svg{flex:none}
.service .label span{font-weight:700;font-size:13.5px;line-height:1.35;text-transform:uppercase;white-space:nowrap}
.service p{margin-top:16px;font-size:6.8px;line-height:2.2;text-align:justify;color:var(--grey);padding:0 6px}
.svc-a{left:30px}.svc-b{left:298px}

.vision-photo{position:absolute;left:0;top:0;width:100%;height:182px;border-bottom:5px solid var(--orange);
  background:linear-gradient(90deg,#6b3a22 0%,#3a4650 35%,#9aa8b4 55%,#5e6a76 75%,#a2633a 100%)}
.vision{position:absolute;left:60px;top:208px;width:190px}
.vision h2,.solution h2{font-weight:900;font-size:23px;line-height:1}
.vision h4,.solution h4{font-weight:400;font-size:7.5px;margin:5px 0 8px}
.vision p,.solution p{font-size:6.4px;line-height:1.8;color:var(--grey)}
.quote{position:absolute;left:296px;top:216px;width:225px;font-size:10px;line-height:1.9}
.quote b{font-weight:700}
.solution-photo{position:absolute;right:0;top:18px;width:290px;height:168px;border-left:5px solid var(--orange);
  background:linear-gradient(135deg,#1d3f7a 0%,#3a5fa8 40%,#8fa2c6 65%,#1a2c55 100%)}
.solution{position:absolute;left:49px;top:52px;width:200px}
.feature{position:absolute;top:210px;width:125px}
.feature h5{font-size:8px;font-weight:700;margin:6px 0 4px}
.feature p{font-size:6.2px;line-height:1.8;color:var(--grey)}
</style>
</head>
<body>

<section class="slide col-l r1">
  <div class="title-block" style="top:50px">
    <div class="brand" style="font-size:24px"><span class="dot"></span>deskrise</div>
  </div>
  <div class="title-block" style="top:140px">
    <h1>HELPING YOU</h1>
    <p class="lower">solve complex business requirements</p>
  </div>
  <div class="url-tag" style="top:257px">WWW.DESKRISE-CONSULT.COM</div>
  <div class="photo photo-ai" role="img" aria-label="Glowing digital brain with circuit lines touched by a robotic and a human hand"></div>
</section>

<section class="slide col-r r1">
  <div class="title-block" style="top:105px">
    <h1>HELPING YOU</h1>
    <p>Solve complex business<br>requirements</p>
  </div>
  <div class="url-tag" style="top:243px">WWW.DESKRISE-CONSULT.COM</div>
  <div class="photo photo-puzzle" role="img" aria-label="Hands joining glowing puzzle pieces">
    <div class="brand" style="top:172px"><span class="dot"></span>deskrise</div>
  </div>
</section>

<section class="slide col-l r2">
  <div class="title-block" style="top:108px">
    <h1>HELPING YOU</h1>
    <p>Solve complex business<br>requirements</p>
  </div>
  <div class="url-tag" style="top:243px">WWW.DESKRISE-CONSULT.COM</div>
  <div class="photo photo-gears" role="img" aria-label="Head filled with gears inside a glowing maze">
    <div class="brand" style="top:262px"><span class="dot"></span>deskrise</div>
  </div>
</section>

<section class="slide col-r r2">
  <div class="title-block" style="top:108px">
    <h1>HELPING YOU</h1>
    <p>Solve complex business<br>requirements</p>
  </div>
  <div class="url-tag" style="top:243px">WWW.DESKRISE-CONSULT.COM</div>
  <div class="photo photo-victory" role="img" aria-label="Silhouette of a businessman raising a fist at sunset">
    <div class="brand" style="top:60px"><span class="dot"></span>deskrise</div>
  </div>
</section>

<section class="slide col-l r3">
  <div class="title-block" style="top:107px">
    <h1>HELPING YOU</h1>
    <p>Solve complex business<br>requirements</p>
  </div>
  <div class="url-tag" style="top:242px">WWW.DESKRISE-CONSULT.COM</div>
  <div class="photo photo-hero" role="img" aria-label="Caped hero silhouette standing above a city at sunrise">
    <div class="brand" style="top:60px"><span class="dot"></span>deskrise</div>
  </div>
</section>

<section class="slide col-r r3">
  <h2 class="centered-title" style="top:18px;font-size:28px">JONAS REITER</h2>
  <p class="centered-title" style="top:52px;font-size:7.5px;font-weight:400;letter-spacing:0">YOUR ADVISOR ON YOUR DIGITAL TRANSFORMATION JOURNEY</p>
  <div class="bio-photo"><div class="inner" role="img" aria-label="Portrait photo of the consultant in a blazer"></div></div>
  <p class="bio-text">I started my professional career over 20 years ago at the global IT Service Provider Corvanet (later acquired by Altrion) while studying Business Informatics at the University of Lindenau. My first contact with IT Service Management and the ITSF framework (v2) was in 2006, later I moved into the ITSM consulting space, first as a vendor-independent Management consultant for Kompassa Consulting (now part of Veltra Group), later as project manager for the German ITSM, SAM and Endpoint management vendor Endwerk.<br><br>There I had my first encounters with LumaDesk in 2016 from a competitor perspective and immediately became hooked on it.</p>
</section>

<section class="slide col-l r4">
  <h2 class="centered-title" style="top:14px;font-size:29px">IN THE LUMADESK ECOSYSTEM</h2>
  <p class="intro">Fascinated by the LumaDesk platform and its capabilities, I moved to the LumaDesk technology partner Taskline (now Clearfin) who offered applications for Telecom and Cloud Service Management on the LumaDesk store, to work as a Customer Success Manager in implementation projects.</p>
  <div class="timeline-line" style="top:118px;height:204px"></div>
  <div class="tl-box right-arrow" style="left:29px;top:103px;width:212px;height:121px">I moved to the implementation partner cirrovo with focus on ITSM and CSM implementations as a Solution Architect and practice lead ITSM to be able to work with the entire LumaDesk platform. I gained project experience with other product suites (Customer Service Management, Field Service Management, Project Portfolio Management) and a broader knowledge of the platform capabilities while working in delivery projects and in pre-sales. Supporting customers with applying the Unified Service Data Model (USDM) structure has also been one of the focus topics in my projects.</div>
  <div class="year" style="top:153px">2018</div>
  <div class="tl-box left-arrow" style="left:332px;top:207px;width:215px;height:82px">Several successful projects and go-live cakes later, I successfully completed the LumaDesk Certified Chief Architect (CCA) program, the pinnacle certification in the LumaDesk ecosystem in 2021. In addition, I revived and intensified my knowledge in the ITSF framework by taking the ITSF 4 Strategic Leader trainings and exams.</div>
  <div class="year" style="top:227px">2021</div>
</section>

<section class="slide col-r r4">
  <h2 class="centered-title" style="top:22px;font-size:28px">ACHIVEMENTS - CERTIFICATIONS</h2>
  <div class="cert-col" style="left:39px">
    <h3>LUMADESK</h3>
    <ul>
      <li>Certified Chief Architect</li>
      <li>Certified Deployment Specialist – ITSM, CSM,<br>FSM, PPM, APM</li>
      <li>Track Certification – ITSM Professional, CSM<br>Professional</li>
      <li>Certified App Builder</li>
      <li>Certified Platform Administrator</li>
    </ul>
  </div>
  <div class="cert-col" style="left:245px">
    <h3>OTHERS</h3>
    <ul>
      <li>ITSF 4 Strategic Leader</li>
      <li>ITSF Foundation v2, v3 and 4</li>
      <li>Certified Sprint Lead I (sprintguild.org)</li>
      <li>PROJEX2 Practitioner</li>
      <li>AgileFlow Foundation</li>
    </ul>
  </div>
  <svg class="cert-badge" width="110" height="152" viewBox="0 0 110 152" aria-hidden="true">
    <defs><linearGradient id="badgeRing" x1="0" y1="0" x2="1" y2="1">
      <stop offset="0" stop-color="#f2d23a"/><stop offset=".5" stop-color="#7cc96a"/><stop offset="1" stop-color="#1fa38a"/></linearGradient></defs>
    <polygon points="55,4 106,32 106,120 55,148 4,120 4,32" fill="#102a33" stroke="url(#badgeRing)" stroke-width="5"/>
  </svg>
</section>

<section class="slide col-l r5">
  <div class="timeline-line" style="top:0;height:78px"></div>
  <div class="tl-box right-arrow" style="left:29px;top:45px;width:212px;height:68px">In February 2023, I decided to go freelance and I am excited to continue helping customers to get the most out of their investment in the Luma platform.<br>At Summit 2023 in Silverton, I had my first speaker appearance when co-presenting a customer's multi-production instance strategy.</div>
  <div class="year" style="top:59px">2023</div>
  <div class="brand" style="position:absolute;left:0;right:0;top:200px;justify-content:center;font-size:34px"><span class="dot"></span>deskrise</div>
</section>

<section class="slide col-r r5">
  <h2 class="portfolio-title">PORTFOLIO</h2>
  <div class="brand portfolio-brand"><span class="dot"></span>deskrise</div>
  <div class="service svc-a">
    <div class="label">
      <svg width="40" height="40" viewBox="0 0 40 40" fill="none" stroke="#fff" stroke-width="2.5" aria-hidden="true"><path d="M12 4v10M12 14l-7 22M12 14l7 22M7 26h10"/><path d="M22 36h14V18z"/></svg>
      <span>Solution design<br>and architecture</span>
    </div>
    <p>Do you feel the need of overarching technical guidance for your LumaDesk platform? Or do you struggle to find experienced solution architects for your projects? Let me help you by providing independent architecture advisory for projects delivered internally or by LumaDesk partners or act as an interims solution architect providing an unbiased support.</p>
  </div>
  <div class="service svc-b">
    <div class="label">
      <svg width="40" height="40" viewBox="0 0 40 40" fill="#fff" aria-hidden="true"><path d="M20 2l2 5h5l-4 3 2 5-5-3-5 3 2-5-4-3h5z"/><path d="M20 16L4 38h32z" fill="none" stroke="#fff" stroke-width="2.5"/><path d="M20 16v22" stroke="#fff" stroke-width="2"/></svg>
      <span>Platform strategy<br>and governance</span>
    </div>
    <p>Are you drowning in daily operations and escalations without a chance to focus on strategic topics? I will help you to develop a long-term strategy and establish a governance structure to allow efficient operation of your LumaDesk platform with an established roadmap, measurable value and a clear decision making process.</p>
  </div>
</section>

<section class="slide col-l r6">
  <h2 class="portfolio-title">PORTFOLIO</h2>
  <div class="brand portfolio-brand"><span class="dot"></span>deskrise</div>
  <div class="service svc-a">
    <div class="label">
      <svg width="40" height="40" viewBox="0 0 40 40" fill="none" stroke="#fff" stroke-width="2.5" aria-hidden="true"><circle cx="19" cy="21" r="16"/><circle cx="19" cy="21" r="10"/><circle cx="19" cy="21" r="4"/><path d="M19 21L34 6M30 4v6h6"/></svg>
      <span>Agile development<br>support</span>
    </div>
    <p>Are you new to the agile development process or your development team needs a little jump-start? I will support you in the sprint planning and refinement, help with the discussions with the stakeholders and requirement gathering as well as with outlining the technical solution approach and making customization/configuration decisions.</p>
  </div>
  <div class="service svc-b">
    <div class="label">
      <svg width="40" height="40" viewBox="0 0 40 40" fill="none" stroke="#fff" stroke-width="2.5" aria-hidden="true"><circle cx="20" cy="20" r="16"/><path d="M20 20l7-9"/><path d="M10 20h3M20 9v3M30 20h-3M12 12l2 2"/></svg>
      <span>Back to out-of-box<br>configuration</span>
    </div>
    <p>Are customizations preventing you from updating to the latest release or making use of the latest new features. I will analyze deviations from the out-of-the-box configuration of your LumaDesk environment and help to get you closer to the baseline configuration to simplify upgrades, reduce overall technical debt and benefit from new features more quickly.</p>
  </div>
</section>

<section class="slide col-r r6">
  <h2 class="portfolio-title">PORTFOLIO</h2>
  <div class="brand portfolio-brand"><span class="dot"></span>deskrise</div>
  <div class="service svc-a">
    <div class="label">
      <svg width="40" height="40" viewBox="0 0 40 40" fill="#fff" aria-hidden="true"><rect x="15" y="3" width="10" height="9"/><rect x="3" y="28" width="10" height="9"/><rect x="15" y="28" width="10" height="9"/><rect x="27" y="28" width="10" height="9"/><path d="M20 12v16M8 28v-7h24v7" fill="none" stroke="#fff" stroke-width="2.5"/></svg>
      <span>Unified service<br>data model (USDM)</span>
    </div>
    <p>Have you ever wondered what the Unified Service Data Model (USDM) is and how you can benefit from it? I will support you in setting up your business service and offering structure to conform with the USDM. This will allow you to effectively measure service levels, take better advantage of the LumaDesk products as well as transparent reporting and service costing.</p>
  </div>
  <div class="service svc-b">
    <div class="label">
      <svg width="40" height="40" viewBox="0 0 40 40" fill="none" stroke="#fff" stroke-width="2.5" aria-hidden="true"><path d="M36 4C26 4 18 10 14 20l6 6c10-4 16-12 16-22z"/><circle cx="26" cy="14" r="3"/><path d="M14 20l-7 1-3 5 8 1M20 26l-1 7-5 3-1-8M9 31l-4 5"/></svg>
      <span>Center of<br>excellence support</span>
    </div>
    <p>Are you building up your internal LumaDesk platform team? Let me help you with on-demand coaching for the team members and by sharing experience from previous projects and LumaDesk best practices. We will jointly look at what's new in the latest releases and I will support you in establishing best practices in the daily operations of the platform.</p>
  </div>
</section>

<section class="slide col-l r7">
  <div class="vision-photo" role="img" aria-label="Hands around a cloud connected to device and network icons"></div>
  <div class="vision">
    <h2>OUR VISION</h2>
    <h4>PLEASE TITTLE TEXT HERE LOREM IPSUM</h4>
    <p>Lorem ipsum dolor sit amet, consectetur adipiscing elit, sed do eiusmod tempor incididunt ut labore et dolore magna aliquat enim ad minim.</p>
  </div>
  <p class="quote">"Don't worry about people stealing your ideas. If your ideas are any good, you'll have to ram them down people's throats."<br><b>- Edda Lorens</b></p>
</section>

<section class="slide col-r r7">
  <div class="solution-photo" role="img" aria-label="Hand touching a network of glowing blue cubes"></div>
  <div class="solution">
    <h2>OUR SOLUTION</h2>
    <h4>PLEASE TITTLE TEXT HERE LOREM</h4>
    <p>Lorem ipsum dolor sit amet, consectetur adipiscing elit, sed do eiusmod tempor incididunt ut labore et dolore magna aliqua. Ut enim ad minim veniam lorem ipsum dolor.</p>
  </div>
  <div class="feature" style="left:49px">
    <svg width="22" height="22" viewBox="0 0 22 22" fill="none" stroke="#f07f2a" stroke-width="1.5" aria-hidden="true"><circle cx="10" cy="12" r="8"/><circle cx="10" cy="12" r="4"/><path d="M10 12l9-9M16 2v4h4"/></svg>
    <h5>Lorem Ipsum Dolor</h5>
    <p>Lorem ipsum dolor sit amet, consectetur adipiscing elit, sed do eius mod tempor lorem ipsum dolor.</p>
  </div>
  <div class="feature" style="left:229px">
    <svg width="22" height="22" viewBox="0 0 22 22" fill="none" stroke="#f07f2a" stroke-width="1.5" aria-hidden="true"><rect x="2" y="2" width="18" height="18"/><rect x="6" y="2" width="10" height="7"/><circle cx="11" cy="14" r="3"/></svg>
    <h5>Lorem Ipsum Dolor</h5>
    <p>Lorem ipsum dolor sit amet, consectetur adipiscing elit, sed do eius mod tempor lorem ipsum dolor.</p>
  </div>
  <div class="feature" style="left:405px">
    <svg width="22" height="22" viewBox="0 0 22 22" fill="none" stroke="#f07f2a" stroke-width="1.5" aria-hidden="true"><circle cx="11" cy="11" r="9"/><path d="M15 7l-2 6-6 2 2-6z"/></svg>
    <h5>Lorem Ipsum Dolor</h5>
    <p>Lorem ipsum dolor sit amet, consectetur adipiscing elit, sed do eius mod tempor lorem ipsum dolor.</p>
  </div>
</section>

</body>
</html>
```